A standard retractable banner is 33" x 81" Create a brand look. Vertical not horizontal.

Harborline Escrow

Requirements
Must have
• MY PHOTO, LOGO, NAME, fb, inst and twitter logo
Nice to have
• Slogan When you think Title, Think Marlo!

```html
<!DOCTYPE html>
<html lang="en">
<head>
<meta charset="utf-8">
<title>Harborline Escrow – Retractable Banner</title>
<link rel="stylesheet" href="https://fonts.googleapis.com/css2?family=Libre+Baskerville:wght@400;700&display=swap">
<style>
  :root {
    --navy: #0e1a4a;
    --green: #0f7a43;
    --green-deep: #136b36;
    --white: #ffffff;
    --page: #e9e9e9;
    --portrait-top: #f4efe9;
    --portrait-bottom: #2a9a55;
  }
  * { margin: 0; padding: 0; box-sizing: border-box; }
  html, body { width: 1200px; height: 1200px; overflow: hidden; background: var(--page); }
  .canvas { position: relative; width: 1200px; height: 1200px; }
  .banner {
    position: absolute; left: 365px; top: 24px;
    width: 510px; height: 1251px;
    transform: scale(0.92); transform-origin: 0 0;
    background: var(--white); overflow: hidden;
    font-family: "Libre Baskerville", Georgia, serif;
  }
  .corner { position: absolute; top: 52px; width: 55px; height: 78px; }
  .corner--navy { left: 0; background: var(--navy); }
  .corner--green { right: 0; background: var(--green-deep); }
  .brand {
    position: absolute; top: 62px; left: 0; width: 100%;
    display: flex; align-items: center; justify-content: center; gap: 14px;
  }
  .brand__dot { width: 46px; height: 46px; border-radius: 50%; background: var(--navy); }
  .brand__name { font-size: 34px; color: var(--navy); letter-spacing: -1px; }
  .headline {
    position: absolute; top: 160px; left: 0; width: 100%;
    text-align: center; color: var(--navy); font-size: 58px; line-height: 74px;
  }
  .tagline {
    position: absolute; top: 312px; left: 0; width: 100%;
    text-align: center; color: var(--green); line-height: 1;
  }
  .tagline__think { display: block; font-size: 52px; margin-left: 30px; }
  .tagline__name { display: block; font-size: 86px; margin-top: -14px; }
  .tagline__cap { font-size: 122px; }
  .portrait {
    position: absolute; left: 62px; top: 475px; width: 424px; height: 560px;
    background: linear-gradient(180deg, var(--portrait-top) 0%, var(--portrait-top) 50%, var(--portrait-bottom) 75%);
    border-radius: 180px 180px 0 0;
  }
  .footer-wave { position: absolute; left: 0; top: 890px; width: 510px; height: 361px; }
  .contact {
    position: absolute; top: 970px; left: 0; width: 100%;
    text-align: center; color: var(--white);
  }
  .contact__phone { font-size: 60px; letter-spacing: 1px; }
  .contact__line { font-size: 28px; line-height: 40px; }
  .social {
    position: absolute; top: 1138px; left: 0; width: 100%;
    display: flex; justify-content: center; gap: 6px;
  }
  .social__icon { width: 66px; height: 66px; border: 2px solid var(--white); border-radius: 50%; }
</style>
</head>
<body>
<div class="canvas">
  <div class="banner">
    <div class="corner corner--navy"></div>
    <div class="corner corner--green"></div>

    <div class="brand">
      <span class="brand__dot"></span>
      <span class="brand__name">Harborline Escrow</span>
    </div>

    <h1 class="headline">WHEN YOU<br>THINK TITLE,</h1>
    <p class="tagline">
      <span class="tagline__think">THINK</span>
      <span class="tagline__name"><span class="tagline__cap">M</span>ARLO!</span>
    </p>

    <div class="portrait" role="img" aria-label="Portrait photo of Marlo, smiling, wearing a green top"></div>

    <svg class="footer-wave" viewBox="0 0 510 361" aria-hidden="true">
      <path d="M0 100 Q250 10 510 8 L510 361 L0 361 Z" fill="var(--navy)"/>
    </svg>

    <div class="contact">
      <p class="contact__phone">555-214-0386</p>
      <p class="contact__line">MReyes@harborline.com</p>
      <p class="contact__line">Marlo.HarborlineIE.com</p>
    </div>

    <div class="social">
      <span class="social__icon" role="img" aria-label="Social profile link"></span>
      <span class="social__icon" role="img" aria-label="Photo sharing profile link"></span>
      <span class="social__icon" role="img" aria-label="Microblog profile link"></span>
    </div>
  </div>
</div>
</body>
</html>
```